General Dental Office Business Card

I run a private general dental office in southern California, and would like a refresh/redesign of my business card. I focus on quality care rather than volume. The email address on the uploaded current card should be updated to: info@marbleshoredental.example. The current card's logo is a deboss, but I am open to other ideas. The logo can be refreshed, but it is something that's been with me since the beginning of the office, so I wouldn't want a drastic redesign.
Target Market(s)
Adults 18-99, whoever needs dental services
Industry/Entity Type
Healthcare/Dental
Contact Information for Business Card
Name, Address, Phone, email
Colors
Designer to choose colors to be used in the design.
Requirements
Must have
- Logo (Same as original one in the uploaded file), space on back for appointment time/date

```html
<!DOCTYPE html>
<html lang="en">
<head>
<meta charset="utf-8">
<title>Marble Shore Dental – Business Card</title>
<link rel="stylesheet" href="https://fonts.googleapis.com/css2?family=Source+Sans+3:ital,wght@0,400;0,600;1,400&display=swap">
<style>
  :root {
    --aqua: #86d5ea;
    --aqua-deep: #2fb4c9;
    --ink: #333333;
    --rule: #8a8a8a;
    --paper: #ffffff;
    --backdrop: #d9d9d9;
  }
  * { box-sizing: border-box; margin: 0; padding: 0; }
  html, body { width: 1200px; height: 800px; overflow: hidden; }
  body {
    background: var(--backdrop);
    font-family: "Source Sans 3", sans-serif;
    display: flex; align-items: center; justify-content: center; gap: 40px;
  }
  .card {
    position: relative; width: 540px; height: 310px;
    background: var(--paper);
    box-shadow: 0 10px 28px rgba(0,0,0,.22);
    overflow: hidden;
  }
  .card__band {
    position: absolute; left: 0; right: 0; bottom: 0; height: 64px;
    background: var(--aqua);
    border-bottom: 3px solid var(--aqua-deep);
    display: flex; align-items: center; color: var(--paper);
  }

  /* front */
  .brand {
    position: absolute; left: 30px; top: 34px; width: 230px;
    display: flex; flex-direction: column; align-items: center;
  }
  .brand__mark {
    width: 96px; height: 96px; border-radius: 50%;
    border: 5px solid var(--aqua);
  }
  .brand__name {
    margin-top: 16px; color: var(--aqua);
    font-size: 27px; font-weight: 400; letter-spacing: .5px; white-space: nowrap;
  }
  .divider {
    position: absolute; left: 282px; top: 30px; width: 1px; height: 180px;
    background: linear-gradient(to bottom, rgba(0,0,0,0), var(--rule) 30%, var(--rule) 70%, rgba(0,0,0,0));
  }
  .contact { position: absolute; left: 302px; top: 34px; right: 14px; }
  .contact__name { color: var(--aqua); font-size: 21px; font-weight: 600; line-height: 1.1; }
  .contact__role { color: var(--ink); font-size: 15px; margin-top: 2px; }
  .contact__list { list-style: none; margin-top: 26px; }
  .contact__item {
    display: flex; align-items: center; gap: 7px;
    color: var(--ink); font-size: 13px; line-height: 1.7; white-space: nowrap;
  }
  .icon { width: 13px; height: 13px; flex: none; }
  .address { padding-left: 30px; gap: 10px; font-size: 16px; letter-spacing: .3px; }
  .address .icon { width: 15px; height: 15px; }

  /* back */
  .appt__mark {
    position: absolute; left: 50%; top: 22px; transform: translateX(-50%);
    display: flex; flex-direction: column; align-items: center;
  }
  .appt__mark .brand__mark { width: 62px; height: 62px; border-width: 4px; }
  .appt__brand { margin-top: 5px; color: var(--aqua); font-size: 13px; letter-spacing: .5px; }
  .appt__title {
    position: absolute; left: 0; right: 0; top: 112px; text-align: center;
    color: var(--aqua); font-size: 26px; font-weight: 600; letter-spacing: .5px;
  }
  .appt__form { position: absolute; left: 70px; right: 70px; top: 160px; }
  .field-row { display: flex; gap: 24px; margin-bottom: 16px; }
  .field {
    flex: 1; display: flex; justify-content: space-between; align-items: flex-end;
    border-bottom: 1px solid var(--rule);
    color: var(--ink); font-size: 15px; padding-bottom: 2px; height: 24px;
  }
  .field--short { flex: 0 0 170px; }
  .appt__note {
    width: 100%; text-align: center; font-style: italic; font-size: 14px; letter-spacing: .2px;
  }
</style>
</head>
<body>

  <section class="card card--front" aria-label="Business card front">
    <div class="brand">
      <div class="brand__mark"></div>
      <div class="brand__name">Marble Shore Dental</div>
    </div>

    <div class="divider"></div>

    <div class="contact">
      <div class="contact__name">Daniel R. Moreau DDS</div>
      <div class="contact__role">General Dentistry</div>
      <ul class="contact__list">
        <li class="contact__item">
          <svg class="icon" viewBox="0 0 16 16" aria-hidden="true"><path fill="var(--aqua)" d="M3.5 1.5l2.5 3-1.5 1.8c.9 2 2.3 3.4 4.2 4.3L10.5 9l3 2.5-1.3 2.3c-.4.6-1.1.8-1.8.6C6 13 3 10 1.6 5.6c-.2-.7 0-1.4.6-1.8z"/></svg>
          555-014-2828
        </li>
        <li class="contact__item">
          <svg class="icon" viewBox="0 0 16 16" aria-hidden="true"><rect x="1" y="3" width="14" height="10" rx="1" fill="var(--aqua)"/><path d="M1.5 3.8L8 9l6.5-5.2" fill="none" stroke="#fff" stroke-width="1.3"/></svg>
          info@marbleshoredental.example
        </li>
        <li class="contact__item">
          <svg class="icon" viewBox="0 0 16 16" aria-hidden="true"><circle cx="8" cy="8" r="7" fill="var(--aqua)"/><g fill="none" stroke="#fff" stroke-width="1"><ellipse cx="8" cy="8" rx="3" ry="7"/><path d="M1 8h14M2.2 4.5h11.6M2.2 11.5h11.6"/></g></svg>
          www.marbleshoredental.example
        </li>
      </ul>
    </div>

    <div class="card__band address">
      <svg class="icon" viewBox="0 0 16 16" aria-hidden="true"><path fill="#fff" d="M8 1a5 5 0 0 0-5 5c0 3.6 5 9 5 9s5-5.4 5-9a5 5 0 0 0-5-5zm0 7a2 2 0 1 1 0-4 2 2 0 0 1 0 4z"/></svg>
      1820 Harbor View Lane Coastville, CA 90000
    </div>
  </section>

  <section class="card card--back" aria-label="Business card back, appointment reminder">
    <div class="appt__mark">
      <div class="brand__mark"></div>
      <div class="appt__brand">Marble Shore Dental</div>
    </div>

    <h1 class="appt__title">Your Next Appointment</h1>

    <div class="appt__form">
      <div class="field-row">
        <div class="field">Name</div>
      </div>
      <div class="field-row">
        <div class="field">Date</div>
        <div class="field field--short">Time <span>am/pm</span></div>
      </div>
    </div>

    <div class="card__band">
      <p class="appt__note">If you are unable to keep the appointment, please give 24 hours notice.</p>
    </div>
  </section>

</body>
</html>
```